Beauty Therapy Web Design

I need a web page design for a small beauty therapy clinic, the owner is currently the only beauty therapist working there.
We require the following pages:
Home
About
Treatments
Nails
Courses
Contact
I will attach the clinics business card, treatment menu and signage so that you get a feeling for the branding colours etc.
This is the first website for the beauty therapist, she would like to attract new clients and also tourists that come in on the cruise ships. The thing that sets her apart from other clinics is that she welcomes texting for appointments.
I have selected refundable because I have never done this before so I don't know what to expect, I have the full intention of going through with it as long as I get a good design.
Feel free to ask for further information
Reason: Project extended as I am away for work and am unable to meet with the owner.
Target Market(s)
Females 18 to 50
Industry/Entity Type
Business
Look and feel
Each slider illustrates characteristics of the customer's brand and the style your logo design should communicate.

```html
<!DOCTYPE html>
<html lang="en">
<head>
<meta charset="utf-8">
<title>Lumera Beauty Therapy</title>
<link rel="stylesheet" href="https://fonts.googleapis.com/css2?family=Arimo:wght@400;700&family=Cormorant+Garamond:ital,wght@1,600;1,700&family=Asap:wght@500;700&display=swap">
<style>
:root{
  --purple:#5b2a8a;
  --purple-dark:#43196e;
  --purple-light:#7a4bb0;
  --violet-text:#5a2aa0;
  --gold:#c49a3c;
  --gold-soft:#d9b35c;
  --cream:#fbe9b4;
  --grey-bg:#e6e6e6;
  --text:#4a4a4a;
  --white:#fff;
  --teal:#2bc3d6;
}
*{box-sizing:border-box;margin:0;padding:0}
html,body{width:1006px;height:1200px;overflow:hidden;background:var(--white)}
body{position:relative;font-family:"Arimo",Arial,sans-serif;color:var(--text);font-size:11.5px}
.abs{position:absolute}
.page-band{left:0;top:122px;width:1006px;height:984px;background:var(--grey-bg);border-top:2px solid #cfcfcf}
.brand{left:109px;top:30px;font-family:"Cormorant Garamond",serif;font-style:italic;font-weight:700;font-size:42px;line-height:46px;color:var(--purple);white-space:nowrap}
.address{right:130px;top:10px;text-align:right;font-size:9px;line-height:12px;color:#555}
.address b{color:var(--gold);font-size:9px}
.phone{right:130px;top:77px;font-size:9px;color:#555}
.phone b{color:var(--gold);font-size:11px;margin-left:2px}
.icon-home{right:110px;top:8px}
.icon-phone{right:106px;top:70px}
.nav{left:105px;top:106px;width:807px;height:33px;border-radius:6px;background:linear-gradient(#7a4bb0,#4a1f78);display:flex;overflow:hidden;box-shadow:0 1px 2px #777}
.nav a{font-family:"Asap",sans-serif;font-weight:700;font-size:10.5px;color:var(--white);text-decoration:none;display:flex;align-items:center;justify-content:center;border-right:1px solid #8a60bd}
.nav a.active{background:linear-gradient(#f3dfae,#d8b572);color:#3a2a18}
.panel{left:91px;top:147px;width:825px;height:943px;background:var(--white)}
.hero{left:98px;top:151px;width:811px;height:313px;background:var(--cream);overflow:hidden}
.hero-photo{left:470px;top:0;width:341px;height:313px;background:linear-gradient(90deg,#efe0d0,#f3d3c2 40%,#eec3ae)}
.hero-title{left:22px;top:12px;font-family:"Asap",sans-serif;font-weight:700;font-size:25px;color:var(--purple)}
.hero-title span{color:var(--gold-soft)}
.hero-list{left:24px;top:54px;list-style:none;font-family:"Asap",sans-serif;font-weight:500;font-size:13.5px;color:#4a3b2a}
.hero-list li{height:22.6px;display:flex;align-items:center;gap:8px}
.btn{background:linear-gradient(#7a4bb0,#4a1f78);color:var(--white);font-family:"Asap",sans-serif;font-weight:700;border-radius:8px;border:2px solid #fff;box-shadow:0 0 0 1px #5b2a8a;display:flex;align-items:center;justify-content:center}
.hero-more{left:282px;top:193px;width:82px;height:28px;font-size:16px}
.thumb-strip{left:98px;top:378px;width:372px;height:86px;background:var(--white)}
.thumb{top:384px;width:122px;height:79px;border:2px solid #ddd}
.arrow{top:408px}
.hero-shadow{left:115px;top:470px;width:760px;height:14px;border-radius:50%;background:radial-gradient(ellipse at center top,rgba(0,0,0,.25),rgba(0,0,0,0) 70%)}
.script{font-family:"Cormorant Garamond",serif;font-style:italic;font-weight:600;color:var(--violet-text)}
.script span{color:var(--gold)}
.welcome{left:101px;top:512px;font-size:25px}
.rule{left:101px;top:550px;width:577px;height:1px;background:#e4e4e4}
.welcome-photo{left:107px;top:568px;width:186px;height:205px;background:linear-gradient(160deg,#3ab4d8,#f1d6c7 55%,#f5f5f0)}
.intro{left:315px;top:567px;width:362px;font-size:11px;line-height:16.8px;color:#555}
.intro p{margin-bottom:6px}
.intro em{font-weight:700;color:#444}
.bullets{left:311px;top:676px;list-style:none;font-size:11.5px;color:var(--violet-text)}
.bullets li{height:29.5px;display:flex;gap:8px}
.bullets li::before{content:"";width:7px;height:7px;border-radius:50%;background:#7b2fd0;margin-top:5px}
.body-copy{left:110px;top:787px;width:568px;font-size:11.5px;line-height:16.8px;color:#444}
.services-h{left:108px;top:862px;font-size:24px}
.services{left:102px;top:899px;width:580px;height:176px;background:#e8e8e8;border-radius:8px}
.services-card{left:123px;top:908px;width:538px;height:157px;background:var(--white)}
.services-photo{left:123px;top:908px;width:103px;height:157px;background:linear-gradient(170deg,#f4e1d6,#eab8a5 55%,#f6c6c9)}
.services-title{left:234px;top:916px;font-size:25px;color:var(--violet-text)}
.services-sub{left:235px;top:946px;font-size:10.5px;font-weight:700;color:#333}
.services-text{left:235px;top:967px;width:413px;font-size:10.7px;line-height:15.2px;color:#555}
.services-more{left:578px;top:1036px;width:66px;height:22px;font-size:13px;border-radius:6px;border-width:1px}
.search-label{left:827px;top:505px;font-family:"Asap",sans-serif;font-weight:700;font-size:15px;color:#7b2fd0;display:flex;align-items:center;gap:6px}
.search{left:709px;top:532px;width:205px;height:36px;border-radius:6px;background:var(--purple-light)}
.search-field{left:719px;top:539px;width:185px;height:21px;border-radius:10px;background:var(--white)}
.promo{left:708px;top:580px;width:204px;height:308px;background:#54237f;border-radius:8px;overflow:hidden}
.promo-head{left:12px;top:16px;width:185px;height:52px;background:#7042a1;color:var(--white);font-family:"Asap",sans-serif;font-weight:700;font-size:15px;line-height:18px;text-align:center;padding-top:8px}
.promo-list{left:18px;top:76px;list-style:none;color:var(--white);font-size:13.5px}
.promo-list li{height:19px;display:flex;gap:7px;align-items:center}
.promo-list li::before{content:"";width:5px;height:5px;border-radius:50%;background:var(--white)}
.promo-value{left:12px;top:139px;width:180px;text-align:right;color:var(--white);font-weight:700;font-size:17px}
.promo-photo{left:10px;top:167px;width:184px;height:131px;background:linear-gradient(135deg,#f6c26a,#f1ebe3 50%,#e9d2c5)}
.ribbon{left:79px;top:264px;width:150px;height:22px;background:var(--teal);transform:rotate(-36deg);color:var(--white);font-family:"Asap",sans-serif;font-weight:700;font-size:14px;text-align:center;line-height:22px}
.chat{left:723px;top:948px;width:188px;height:119px;border:1px solid #ccc;border-radius:8px;background:linear-gradient(#fff,#ebebeb)}
.chat-icon{left:708px;top:922px;width:46px;height:44px;border-radius:50%;background:linear-gradient(#f6b944,#d6282a)}
.chat-name{left:760px;top:925px;font-weight:700;font-size:19px;color:var(--purple-dark)}
.chat-tag{left:757px;top:964px;font-size:8.5px;font-weight:700;color:#222}
.chat-close{left:883px;top:973px;font-size:7px;color:#444}
.chat-ask{left:734px;top:1016px;width:166px;text-align:center;font-size:7.5px;line-height:10px;color:#333}
.chat-actions{left:785px;top:1038px;font-size:9.5px;color:#333;display:flex;gap:12px}
.chat-foot{left:742px;top:1056px;font-size:6px;color:#444}
.footer-rule{left:0;top:1106px;width:1006px;height:2px;background:#d2d2d2}
.footer-links{left:110px;top:1137px;font-size:11.5px;color:#444;word-spacing:3px}
.footer-links span{margin:0 7px;color:#444}
.copyright{left:109px;top:1158px;font-size:10.5px;color:#333}
.social{top:1133px;width:110px;text-align:center;font-size:8px;color:#888}
.social b{display:block;margin-top:7px;font-size:13px;color:#2b62b4}
.social.chirper b{color:#3bb5e0}
.vline{top:1124px;width:1px;height:62px;background:#ddd}
.feed-square{width:36px;height:18px;background:#e2671e;margin:8px auto 0}
</style>
</head>
<body>
<div class="abs page-band"></div>

<header>
  <div class="abs brand">Lumera Beauty Therapy</div>
  <svg class="abs icon-home" width="18" height="16" viewBox="0 0 18 16"><path d="M9 1 1 8h2.5v7h4v-4.5h3V15h4V8H17z" fill="#6a2fb0"/></svg>
  <div class="abs address"><b>WESTBROOK</b><br>28 Harbour Lane<br>Westbrook NSW 2100</div>
  <svg class="abs icon-phone" width="16" height="20" viewBox="0 0 16 20"><path d="M12 1c2 1 3 3 2 5l-2 1c-1-1-2-1-2 0L8 13c0 1 1 1 2 1l-1 2c-2 2-5 1-5-1C4 9 8 3 12 1z" fill="#7b2fd0"/></svg>
  <div class="abs phone">Telephone: <b>02 5550 0148</b></div>
  <nav class="abs nav">
    <a class="active" style="width:70px">HOME</a>
    <a style="width:80px">ABOUT</a>
    <a style="width:120px">TREATMENTS</a>
    <a style="width:94px">NAILS</a>
    <a style="width:118px">COURSES</a>
    <a style="width:135px;border-right:0">CONTACT</a>
  </nav>
</header>

<div class="abs panel"></div>

<section>
  <div class="abs hero">
    <div class="abs hero-photo" role="img" aria-label="Spa stones beside a woman with clear skin and pink lily flowers"></div>
    <h1 class="abs hero-title">Lumera <span>Beauty Therapy</span></h1>
    <ul class="abs hero-list">
      <li><svg width="14" height="12"><path d="M1 6l4 4 8-9" stroke="#5b2a8a" stroke-width="3" fill="none"/></svg>Facials</li>
      <li><svg width="14" height="12"><path d="M1 6l4 4 8-9" stroke="#5b2a8a" stroke-width="3" fill="none"/></svg>Waxing</li>
      <li><svg width="14" height="12"><path d="M1 6l4 4 8-9" stroke="#5b2a8a" stroke-width="3" fill="none"/></svg>Acrylic &amp; Gel Nails</li>
      <li><svg width="14" height="12"><path d="M1 6l4 4 8-9" stroke="#5b2a8a" stroke-width="3" fill="none"/></svg>Eye lash Brow tints</li>
      <li><svg width="14" height="12"><path d="M1 6l4 4 8-9" stroke="#5b2a8a" stroke-width="3" fill="none"/></svg>Manicures / Pedicures</li>
      <li><svg width="14" height="12"><path d="M1 6l4 4 8-9" stroke="#5b2a8a" stroke-width="3" fill="none"/></svg>spray tans</li>
    </ul>
    <div class="abs btn hero-more">More</div>
  </div>
  <div class="abs thumb-strip"></div>
  <svg class="abs arrow" style="left:111px" width="20" height="34"><path d="M19 0v34L0 17z" fill="#2e2540"/></svg>
  <div class="abs thumb" style="left:152px;background:linear-gradient(90deg,#c58a5c,#9c5f3b)" role="img" aria-label="Toned waist after body treatment"></div>
  <div class="abs thumb" style="left:291px;background:linear-gradient(135deg,#8aa3b8,#e0c7b4)" role="img" aria-label="Therapist giving a facial treatment"></div>
  <div class="abs thumb" style="left:429px;background:linear-gradient(135deg,#f2efe9,#c99479)" role="img" aria-label="Woman relaxing during a back massage"></div>
  <svg class="abs arrow" style="left:577px" width="20" height="34"><path d="M1 0v34L20 17z" fill="#2e2540"/></svg>
  <div class="abs hero-shadow"></div>
</section>

<main>
  <h2 class="abs script welcome">Welcome to <span>Lumera Beauty Therapy</span></h2>
  <div class="abs rule"></div>
  <div class="abs welcome-photo" role="img" aria-label="Woman receiving a relaxing head massage by a pool with white flowers"></div>
  <div class="abs intro">
    <p><em>Lorem Ipsum is simply dummy text of the printing and typesetting industry. Lorem Ipsum</em> has been the industry's standard dummy text ever since the 1500s,</p>
    <p>Simply dummy text of the printing and typesetting industry. Lorem Ipsum has been.</p>
  </div>
  <ul class="abs bullets">
    <li>When an unknown printer took a galley of type and scramb</li>
    <li>When an unknown printer took a galley of type and scramb</li>
    <li>When an unknown printer took a galley of type and scramb</li>
  </ul>
  <p class="abs body-copy">It was popularised in the 1960s with the release of Quickset sheets containing Lorem Ipsum passages, and more recently with desktop publishing software like PageForm including versions of Lorem Ipsum.It was popularised in the 1960s with the release of.</p>

  <h2 class="abs script services-h">Our <span>Services</span></h2>
  <div class="abs services"></div>
  <svg class="abs" style="left:106px;top:974px" width="12" height="26"><path d="M11 0v26L0 13z" fill="#999"/></svg>
  <svg class="abs" style="left:667px;top:974px" width="12" height="26"><path d="M1 0v26L12 13z" fill="#999"/></svg>
  <div class="abs services-card"></div>
  <div class="abs services-photo" role="img" aria-label="Woman with smooth skin holding a pink lily"></div>
  <h3 class="abs script services-title">Laser Hair Removal</h3>
  <div class="abs services-sub">Solace - Pulse Seven Certified.</div>
  <p class="abs services-text">Lorem Ipsum is simply dummy text of the printing and typesetting industry. Lorem Ipsum has been the industry's standard dummy text ever since the 1500s,Lorem Ipsum is simply dummy text of the printing and typesetting industry. Lorem Ipsum has been the industry's standard dummy text ever since the 1500s,</p>
  <div class="abs btn services-more">More.</div>
</main>

<aside>
  <div class="abs search-label"><svg width="20" height="20"><circle cx="12" cy="8" r="6" fill="none" stroke="#888" stroke-width="2"/><path d="M8 12l-6 6" stroke="#888" stroke-width="3"/></svg>Search</div>
  <div class="abs search"></div>
  <div class="abs search-field"></div>

  <div class="abs promo">
    <div class="abs promo-head">LET YOUR SKIN GLOW<br>WITH VITAMIN A</div>
    <ul class="abs promo-list"><li>Vitamin Infusion</li><li>Eyebrow Shape</li><li>Ultra A Facial Cream</li></ul>
    <div class="abs promo-value">Value $163</div>
    <div class="abs promo-photo" role="img" aria-label="Woman relaxing with a facial mask beside orange flowers"></div>
    <div class="abs ribbon">Now $89</div>
  </div>

  <div class="abs chat"></div>
  <div class="abs chat-icon" role="img" aria-label="Support agent headset icon"></div>
  <div class="abs chat-name">chat desk</div>
  <div class="abs chat-tag">website instant messenger</div>
  <div class="abs chat-close">close</div>
  <div class="abs chat-ask">Would you like to accept a Live Help chat with one of our staff members?</div>
  <div class="abs chat-actions"><span><b style="color:#2a9a2a">&#10003;</b> accept</span><span><b style="color:#d33">&#10007;</b> decline</span></div>
  <div class="abs chat-foot">chatdesk.example live support</div>
</aside>

<footer>
  <div class="abs footer-rule"></div>
  <div class="abs footer-links">Home<span>|</span>About<span>|</span>Treatments<span>|</span>Nails<span>|</span>Courses<span>|</span>Contact</div>
  <div class="abs copyright">© 2012 Lumera Beauty Therapy , Inc. All rights reserved.</div>
  <div class="abs social" style="left:560px">Find us on Friendbook<b>Friendbook</b></div>
  <div class="abs vline" style="left:678px"></div>
  <div class="abs social chirper" style="left:680px">Follow us on Chirper<b>Chirper</b></div>
  <div class="abs vline" style="left:788px"></div>
  <div class="abs social" style="left:799px">Subscribe our Feedline feed<div class="feed-square"></div></div>
</footer>
</body>
</html>
```